Brisk Harbor Packaging Design for RTE Beans

We need a product mock design that is aligned with our brand image. We need three SKUs. Black bean, Pinto bean, and Chickpeas. I've uploaded our brand logo here, Brisk Harbor. I have also took a screenshot of the design elements that we would like to see. The packaging die line can be seen on the file "packaging sample". Please refer to the screenshots for packaging design directions.

```html
<!DOCTYPE html>
<html lang="en">
<head>
<meta charset="utf-8">
<title>Brisk Harbor – Drifter Black Beans Pouch</title>
<link rel="stylesheet" href="https://fonts.googleapis.com/css2?family=Alfa+Slab+One&family=Old+Standard+TT:wght@700&family=Libre+Baskerville:wght@700&display=swap">
<style>
  :root {
    --cream: #ebe1c5;
    --cream-light: #efe6cd;
    --cream-shade: #d9cdaa;
    --olive: #7b8660;
    --red: #cf222d;
    --ink: #3b3536;
    --bean: #25262c;
  }
  * { margin: 0; padding: 0; box-sizing: border-box; }
  html, body { width: 776px; height: 1200px; overflow: hidden; background: var(--cream); }
  .pouch { position: relative; width: 776px; height: 1200px; background: var(--cream); overflow: hidden; }

  .seal-band { position: absolute; left: 0; top: 0; width: 776px; height: 242px; background: var(--olive); }
  .die-lines { position: absolute; left: 0; top: 0; }

  .front-frame {
    position: absolute; left: 41px; top: 287px; width: 699px; height: 876px;
    border: 10px solid var(--olive);
  }

  .mascot-art {
    position: absolute; left: 288px; top: 320px; width: 206px; height: 270px;
    background: radial-gradient(ellipse at 50% 45%, #b9ae95 0%, var(--cream-shade) 75%);
    border-radius: 6px;
  }

  .brand-name {
    position: absolute; left: 0; top: 628px; width: 776px; text-align: center;
    font-family: "Libre Baskerville", serif; font-weight: 700; font-size: 44px;
    letter-spacing: 4px; line-height: 56px; color: var(--ink);
  }

  .product-name { position: absolute; left: 0; top: 722px; width: 776px; }
  .product-name text { font-family: "Alfa Slab One", serif; fill: var(--olive); }

  .bean-photo {
    position: absolute; left: 186px; top: 831px; width: 411px; height: 159px;
    background: radial-gradient(ellipse at 40% 40%, #3c3e47 0%, var(--bean) 60%, #15161a 100%);
  }

  .flavor-banner {
    position: absolute; left: 91px; top: 1003px; width: 599px; height: 53px;
    background: var(--olive); border-radius: 8px;
    display: flex; align-items: center; justify-content: center;
    font-family: "Old Standard TT", serif; font-weight: 700; font-size: 25px;
    letter-spacing: 3px; color: var(--cream-light);
  }

  .spec-row { position: absolute; left: 0; top: 1063px; width: 776px; height: 78px; }
  .spec-claims {
    position: absolute; right: 469px; top: 22px; text-align: right;
    font-family: "Libre Baskerville", serif; font-weight: 700; font-size: 19px; line-height: 23px; color: var(--ink);
  }
  .spec-divider { position: absolute; top: 2px; width: 4px; height: 72px; background: var(--ink); }
  .spec-divider.left { left: 327px; }
  .spec-divider.right { left: 495px; }
  .spec-heat { position: absolute; left: 333px; top: 0; width: 160px; }
  .spec-heat text { font-family: "Alfa Slab One", serif; fill: var(--ink); }
  .spec-weight {
    position: absolute; left: 522px; top: 22px;
    font-family: "Libre Baskerville", serif; font-weight: 700; font-size: 19px; line-height: 23px; color: var(--ink);
  }
</style>
</head>
<body>
<main class="pouch">
  <div class="seal-band"></div>

  <svg class="die-lines" width="776" height="1200" viewBox="0 0 776 1200">
    <g stroke="var(--red)" stroke-width="3" fill="none">
      <line x1="0" y1="168" x2="776" y2="168"/>
      <line x1="0" y1="204" x2="776" y2="204"/>
      <line x1="0" y1="241" x2="776" y2="241"/>
      <line x1="45" y1="20" x2="45" y2="268" stroke-dasharray="17 12"/>
      <line x1="736" y1="20" x2="736" y2="268" stroke-dasharray="17 12"/>
      <polyline points="0,122 14,122 19,132 14,142 0,142"/>
      <polyline points="776,122 766,122 761,132 766,142 776,142"/>
    </g>
  </svg>

  <div class="front-frame"></div>
  <svg class="die-lines" width="776" height="1200" viewBox="0 0 776 1200">
    <g stroke="var(--red)" stroke-width="2.5" fill="none" stroke-dasharray="17 12">
      <line x1="45" y1="292" x2="45" y2="1154"/>
      <line x1="736" y1="292" x2="736" y2="1154"/>
      <line x1="45" y1="1154" x2="736" y2="1154"/>
    </g>
  </svg>

  <div class="mascot-art" role="img" aria-label="Illustration of the brand mascot holding wheat stalks"></div>

  <p class="brand-name">BRISK HARBOR</p>

  <svg class="product-name" width="776" height="90" viewBox="0 0 776 90">
    <text x="390" y="80" text-anchor="middle" font-size="78" textLength="625" lengthAdjust="spacingAndGlyphs">DRIFTER BLACK BEANS</text>
  </svg>

  <div class="bean-photo" role="img" aria-label="Photo of dry black beans"></div>

  <div class="flavor-banner">WHIT ONIONS AND BELL PEPPER</div>

  <section class="spec-row">
    <p class="spec-claims">NON-GMO<br>PLANT PROTEIN</p>
    <span class="spec-divider left"></span>
    <svg class="spec-heat" width="160" height="78" viewBox="0 0 160 78">
      <text x="80" y="62" text-anchor="middle" font-size="52" textLength="108" lengthAdjust="spacingAndGlyphs">MILD</text>
    </svg>
    <span class="spec-divider right"></span>
    <p class="spec-weight">NET.WT.<br>10 OZ (283 G)</p>
  </section>
</main>
</body>
</html>
```